Endocrinologist needs new stationery

I have a logo from MarkForge and now need stationery with the new logo.

Address: Suite 4, 282 Falcon Street, Richmond, VIC 3121
Phone: 03 9417 2253
Fax: 03 9417 2255
Website: www.drmaylacorwen.com.au
Email: admin@drmaylacorwen.com.au

```html
<!DOCTYPE html>
<html lang="en">
<head>
<meta charset="utf-8">
<title>Dr Mayla Corwen — Stationery</title>
<link href="https://fonts.googleapis.com/css2?family=Montserrat:wght@400;500&family=Arimo:wght@400&family=Tinos:wght@400;700&display=swap" rel="stylesheet">
<style>
  :root{
    --canvas:#ececec;
    --paper:#f7f7f7;
    --brand-blue:#356a93;
    --ink:#3a3a3a;
    --ink-soft:#6b6b6b;
    --rule:#b9b9b9;
    --silver:#e3e6ea;
    --window:#e6e6e6;
  }
  *{box-sizing:border-box;margin:0;padding:0}
  html,body{width:1200px;height:795px;overflow:hidden;background:var(--canvas)}
  .canvas{position:relative;width:1200px;height:795px;background:var(--canvas);overflow:hidden}
  .sheet{position:absolute;background:var(--paper);box-shadow:0 1px 3px rgba(0,0,0,.12)}

  .wordmark{font-family:"Montserrat",sans-serif;font-weight:400;color:var(--brand-blue);white-space:nowrap;letter-spacing:.04em;line-height:1}

  /* Letterhead */
  .letterhead{left:292px;top:99px;width:293px;height:415px}
  .letterhead .wordmark{position:absolute;left:0;right:0;top:26px;text-align:center;font-size:17px}
  .letterhead .copy{position:absolute;left:35px;width:222px;font-family:"Arimo",sans-serif;color:var(--ink);font-size:4.6px;line-height:6.4px}
  .recipient{top:105px}
  .salutation{top:162px}
  .body-text{top:175px}
  .body-text p{text-align:justify;margin-bottom:6.4px}
  .signoff{top:271px}
  .signature{position:absolute;left:35px;top:283px;width:66px;height:24px;background:linear-gradient(90deg,#e9e9e9,#f1f1f1)}
  .signatory{top:315px}
  .letterhead .footer-rule{position:absolute;left:35px;width:222px;top:373px;border-top:.6px solid var(--rule)}
  .letterhead .footer{position:absolute;left:0;right:0;top:380px;text-align:center;font-family:"Montserrat",sans-serif;font-size:5.6px;line-height:6.8px;color:var(--ink-soft)}
  .footer .label{color:var(--brand-blue);font-weight:500}

  /* Presentation folder */
  .folder{position:absolute;left:637px;top:80px;width:345px;height:436px;background:var(--brand-blue);box-shadow:0 1px 3px rgba(0,0,0,.15)}
  .folder .spine{position:absolute;top:0;bottom:0;width:.8px;background:rgba(0,0,0,.18)}
  .folder .spine.one{left:5px}
  .folder .spine.two{left:18px}
  .folder .wordmark{position:absolute;left:35px;top:380px;font-size:16px;color:var(--silver)}

  /* Business card */
  .business-card{left:187px;top:551px;width:131px;height:74px}
  .business-card .wordmark{position:absolute;left:16px;top:13px;font-size:9px}
  .business-card .contact{position:absolute;left:16px;top:42px;font-family:"Montserrat",sans-serif;font-size:3.3px;line-height:4.3px;color:var(--ink)}
  .business-card .contact .label{color:var(--brand-blue);font-weight:500}
  .business-card .address{position:absolute;left:16px;top:61px;font-family:"Montserrat",sans-serif;font-size:3.3px;color:var(--ink)}

  /* Appointment card */
  .appointment-card{left:187px;top:646px;width:131px;height:75px}
  .appointment-card .wordmark{position:absolute;left:0;right:0;text-align:center;top:11px;font-size:9px}
  .appointment-card .heading{position:absolute;left:0;right:0;top:32px;text-align:center;font-family:"Tinos",serif;font-weight:700;font-size:5.4px;color:var(--brand-blue);letter-spacing:.02em}
  .appointment-card .field{position:absolute;left:14px;font-family:"Tinos",serif;font-size:3.2px;color:var(--ink);display:flex;align-items:flex-end;gap:2px}
  .appointment-card .field .line{border-bottom:.4px solid var(--ink-soft);height:3px}
  .field.date{top:44px}
  .field.time{top:44px;left:67px}
  .field.details{top:54px}
  .appointment-card .notice{position:absolute;left:0;right:0;top:63px;text-align:center;font-family:"Montserrat",sans-serif;font-size:2.6px;line-height:3.4px;color:var(--ink)}

  /* DL envelope front */
  .envelope-front{left:353px;top:561px;width:329px;height:157px}
  .envelope-front .wordmark{position:absolute;left:26px;top:27px;font-size:11px}
  .envelope-front .return-address{position:absolute;left:10px;width:130px;top:47px;text-align:center;font-family:"Montserrat",sans-serif;font-size:6px;line-height:7.2px;color:var(--ink-soft)}
  .envelope-front .window{position:absolute;left:29px;top:100px;width:88px;height:32px;border-radius:3px;background:var(--window);border:.6px solid #d4d4d4}

  /* Envelope back */
  .envelope-back{left:713px;top:561px;width:329px;height:157px}
  .envelope-back .flap{position:absolute;left:0;top:0;width:329px;height:56px}
  .envelope-back .wordmark{position:absolute;left:0;right:0;text-align:center;top:23px;font-size:13px;color:#ffffff}
</style>
</head>
<body>
<main class="canvas">

  <article class="sheet letterhead">
    <div class="wordmark">Dr Mayla Corwen</div>
    <div class="copy recipient">First Name Last Name<br>Addressee's name<br>Building number/name and street<br>Post Town, Post Code</div>
    <div class="copy salutation">Dear First Name</div>
    <div class="copy body-text">
      <p>Lorem ipsum dolor sit amet, consectetur adipiscing elit. Vestibulum eu vulputate sapien. In quis imperdiet lectus, eget accumsan sem. Vestibulum consequat rhoncus cursus. Quisque ultrices facilisis libero, eu facilisis nisl congue sit amet. Phasellus consequat justo mi. In sollicitudin justo sed eros blandit, non eleifend elit faucibus. Aliquam elit purus, facilisis at pulvinar eu, rutrum ut mauris. Suspendisse aliquam ipsum vitae egestas venenatis. Quisque a lacinia orci, sit amet tincidunt diam. Nulla blandit justo sit amet purus gravida, pulvinar iaculis sapien egestas. Sed vehicula diam leo, et vehicula leo elementum et. Duis nec suscipit justo. Maecenas eget pretium leo. Quisque imperdiet ut quam ut placerat. Duis facilisis, nisi sit amet dictum egestas, neque nulla elementum nibh, in ultrices mi magna nec metus.</p>
      <p>Duis arcu lacus, accumsan id lectus eu, condimentum tincidunt purus. Cras ac justo sed odio mattis gravida consectetur ac sapien. Integer eleifend enim et ipsum fermentum auctor. Quisque at porttitor velit. Aenean gravida nibh odio, eget tempus mauris semper at. In consectetur sed leo ut molestie. Sed pharetra urna quis turpis fringilla, ut posuere massa hendrerit. Proin pulvinar nibh augue, vel luctus elit aliquet non. Nunc elementum iaculis turpis eu interdum. Pellentesque non imperdiet magna, ut facilisis augue.</p>
    </div>
    <div class="copy signoff">Sincerely,</div>
    <div class="signature" role="img" aria-label="Handwritten signature"></div>
    <div class="copy signatory">First Name Last Name<br>Position</div>
    <div class="footer-rule"></div>
    <div class="footer">
      Suite 4, 282 Falcon Street, Richmond, VIC 3121<br>
      <span class="label">T :</span> 03 9417 2253 &nbsp;<span class="label">F :</span> 03 9417 2255 &nbsp;<span class="label">E :</span> admin@drmaylacorwen.com.au<br>
      www.drmaylacorwen.com.au
    </div>
  </article>

  <article class="folder">
    <span class="spine one"></span>
    <span class="spine two"></span>
    <div class="wordmark">Dr Mayla Corwen</div>
  </article>

  <article class="sheet business-card">
    <div class="wordmark">Dr Mayla Corwen</div>
    <div class="contact">
      <span class="label">T :</span> 03 9417 2253 <span class="label">F :</span> 03 9417 2255<br>
      admin@drmaylacorwen.com.au<br>
      www.drmaylacorwen.com.au
    </div>
    <div class="address">Suite 4, 282 Falcon Street, Richmond, VIC 3121</div>
  </article>

  <article class="sheet appointment-card">
    <div class="wordmark">Dr Mayla Corwen</div>
    <div class="heading">YOUR NEXT APPOINTMENT</div>
    <div class="field date">Date: <span class="line" style="width:40px"></span></div>
    <div class="field time">Time: <span class="line" style="width:42px"></span></div>
    <div class="field details">Details: <span class="line" style="width:90px"></span></div>
    <div class="notice">IF YOU ARE UNABLE TO KEEP YOUR APPOINTMENT,<br>PLEASE CONTACT US AS SOON AS POSSIBLE.</div>
  </article>

  <article class="sheet envelope-front">
    <div class="wordmark">Dr Mayla Corwen</div>
    <div class="return-address">Suite 4, 282 Falcon Street,<br>Richmond, VIC 3121</div>
    <div class="window"></div>
  </article>

  <article class="sheet envelope-back">
    <svg class="flap" viewBox="0 0 329 56" aria-hidden="true">
      <path d="M0 0 H329 L322 48 Q321 55 313 55 H16 Q8 55 7 48 Z" fill="var(--brand-blue)"/>
    </svg>
    <div class="wordmark">Dr Mayla Corwen</div>
  </article>

</main>
</body>
</html>
```